Tavenored Crest

Need very crisp business cards for Tavenor Crest per the logo attached. The vision of Tavenor Crest is 'Steer every Venture to Tavenor'. I am going into Freelance | Consulting | Contracting and need this communicated on the card. I need the card to provide a clear message of professionalism and what the vision emulates. Will need an area for my website, LinkedIn, Twitter, as fell as the obvious Name, Address, phone, email... on the back, I would like the Vision but receptive to your design ideas.

```html
<!DOCTYPE html>
<html lang="en">
<head>
<meta charset="utf-8">
<title>Tavenored Crest — Business Card</title>
<link href="https://fonts.googleapis.com/css2?family=Arimo:wght@400;700&display=swap" rel="stylesheet">
<style>
  :root {
    --backdrop: #2a2a2c;
    --card: #ffffff;
    --navy: #2b3f86;
    --ink: #2f2f33;
    --text: #3a3a3e;
    --muted: #6a6c75;
    --faint: #e9ebf2;
    --accent-dot: #3b8fd9;
  }
  * { box-sizing: border-box; margin: 0; padding: 0; }
  html, body {
    width: 1200px; height: 880px; overflow: hidden;
    background: var(--backdrop);
    font-family: "Arimo", Arial, sans-serif;
  }
  .canvas { position: relative; width: 1200px; height: 880px; }
  .card {
    position: absolute; left: 250px; width: 700px; height: 400px;
    background: var(--card); overflow: hidden;
    box-shadow: 0 12px 30px rgba(0,0,0,.45);
  }
  .card--front { top: 20px; }
  .card--back { top: 460px; }

  .brand { position: absolute; display: flex; flex-direction: column; align-items: flex-end; }
  .wordmark {
    display: flex; align-items: center; gap: 12px;
    color: var(--navy); font-weight: 400; white-space: nowrap; line-height: 1;
  }
  .wordmark__mark { background: var(--navy); flex: none; }
  .tagline {
    color: var(--muted); text-transform: uppercase; white-space: nowrap;
    letter-spacing: .22em; margin-top: 6px;
  }

  .card--front .brand { left: 140px; top: 164px; }
  .card--front .wordmark { font-size: 46px; }
  .card--front .wordmark__mark { width: 40px; height: 40px; }
  .card--front .tagline { font-size: 10px; }
  .front__site {
    position: absolute; right: 150px; bottom: 96px;
    font-size: 18px; color: var(--text);
  }

  .back__emblem {
    position: absolute; left: 360px; top: -40px; width: 250px; height: 250px;
    background: var(--faint);
  }
  .card--back .brand { right: 40px; top: 58px; }
  .card--back .wordmark { font-size: 36px; }
  .card--back .wordmark__mark { width: 30px; height: 30px; }
  .card--back .tagline { font-size: 8.5px; }
  .rule { position: absolute; height: 1.5px; background: var(--navy); }
  .rule--top { left: 200px; right: 40px; top: 128px; }
  .rule--bottom { left: 40px; width: 210px; top: 292px; }

  .person { position: absolute; left: 40px; top: 150px; }
  .person__name { font-size: 26px; font-weight: 700; color: var(--ink); }
  .person__role { font-size: 18px; color: var(--navy); margin-top: 4px; }

  .contacts {
    position: absolute; right: 40px; top: 146px; list-style: none;
    font-size: 16px; color: var(--text); text-align: right; line-height: 1.5;
  }
  .contacts li { display: flex; justify-content: flex-end; align-items: center; gap: 8px; }
  .contacts svg { width: 14px; height: 14px; fill: var(--navy); }

  .address {
    position: absolute; left: 40px; top: 304px;
    font-size: 18px; line-height: 1.35; color: var(--text); font-style: normal;
  }
  .socials {
    position: absolute; right: 40px; bottom: 60px;
    display: flex; align-items: center; gap: 14px;
    font-size: 17px; color: var(--text);
  }
  .socials__item { display: flex; align-items: center; gap: 8px; }
  .socials__dot { width: 12px; height: 12px; border-radius: 50%; background: var(--accent-dot); }
  .socials__square { width: 12px; height: 12px; background: var(--navy); }
  .socials__sep { color: var(--navy); }
</style>
</head>
<body>
<main class="canvas">
  <section class="card card--front">
    <div class="brand">
      <div class="wordmark"><span class="wordmark__mark"></span>Tavenored Crest</div>
      <p class="tagline">Steer every Venture to Tavenor</p>
    </div>
    <p class="front__site">www.tavenoredcrest.com</p>
  </section>

  <section class="card card--back">
    <div class="back__emblem"></div>
    <div class="brand">
      <div class="wordmark"><span class="wordmark__mark"></span>Tavenored Crest</div>
      <p class="tagline">Steer every Venture to Tavenor</p>
    </div>
    <div class="rule rule--top"></div>

    <div class="person">
      <p class="person__name">Marcus Delaney</p>
      <p class="person__role">Managing Director</p>
    </div>

    <ul class="contacts">
      <li>214-555-0187
        <svg viewBox="0 0 24 24"><path d="M6.6 10.8a15.2 15.2 0 0 0 6.6 6.6l2.2-2.2a1 1 0 0 1 1-.25 11.4 11.4 0 0 0 3.6.57 1 1 0 0 1 1 1V20a1 1 0 0 1-1 1A17 17 0 0 1 3 4a1 1 0 0 1 1-1h3.5a1 1 0 0 1 1 1c0 1.25.2 2.45.57 3.6a1 1 0 0 1-.25 1z"/></svg>
      </li>
      <li>marcus@tavenoredmail.com
        <svg viewBox="0 0 24 24"><path d="M2 5h20v14H2z M2 5l10 8 10-8" fill="none" stroke="#2b3f86" stroke-width="2.2"/></svg>
      </li>
      <li>www.tavenorsite.com
        <svg viewBox="0 0 24 24"><circle cx="12" cy="12" r="9" fill="none" stroke="#2b3f86" stroke-width="2"/><path d="M3 12h18M12 3c3 3 3 15 0 18M12 3c-3 3-3 15 0 18" fill="none" stroke="#2b3f86" stroke-width="1.6"/></svg>
      </li>
    </ul>

    <div class="rule rule--bottom"></div>
    <address class="address">118 Harlow Street NE<br>Suite 210, Grand Rapids<br>MI 49506</address>

    <div class="socials">
      <span class="socials__item"><span class="socials__dot"></span>Tavenoredcrest</span>
      <span class="socials__sep">/</span>
      <span class="socials__item"><span class="socials__square"></span>Tavenoredcrest</span>
    </div>
  </section>
</main>
</body>
</html>
```